Suchen ansprechendes & seriöses Urkunden/Zertifikat Design für Webseite & Druck
Zielgruppe
Auf unserer Webseite http://gruen-im-herbst.de können sich Unternehmen, Institutionen und Vereine ihre Seniorenfreundlichkeit durch ein Zertifikat bestätigen und zertifizieren lassen.
Unsere Kundengruppen: Hotel – Gastronomie – Wellness – Reisen und Touristik – Touristikregionen – Seniorenshop – Onlineshop – Unternehmen als Dienstleister – Medizin und Health-Service – Apotheke – Altenheim – Pflegeheim – Seniorenheim – Vereine – Seniorenservice – Zahnärzte – Fitnessstudio – Sportstudio – Physiotherapie – Sportverein – Golfclub – und viele weitere seniorenfreundliche Institutionen.
Aufgabenstellung
Auftrag- Ausschreibung:
- Erstellung eines Design:
- Urkunde für Webseite gruen-im-herbst.de - Das Zertifikat "Grün im Herbst“
Funktion:
Kunde erkennt das Zertifikat - Logo auf einer Webseite und Klickt auf dieses.
Er wird weitergeleitet auf eine Unterseite, worin die Richtlinien und die Urkunde sichtbar wird.
Zielgruppe:
- Unternehmen, welche das Zertifikat auf Ihre Webseite setzen. Die Urkunde gibt Auskunft, dass der Dienstleister einen besonderen Service für Senioren ausübt. Die Urkunde ist sichtbar auf der Webseite, indem das Logo angeklickt wird. Die Urkunde gibt es ebenfalls als Download, damit der Kunde diese in seinen Geschäftsräumen aufhängen kann oder diese in seinen Werbeunterlagen präsentieren kann.
- Verbraucher sollen beeindruckt sein, von der Urkunde, welches Vertrauen ausstrahlt, aber auch Seriosität
Folgende Ausstrahlung soll die Urkunde haben:
- Soll Mitbewerber des Zertifikatsinhaber beeindrucken und das Verlangen aufzeigen, sich ebenfalls zertifizieren zu lassen ( ca: 70% der Kunden sind Mitbewerber … ). Nach dem Motto "Das Logo ist super und edel, das muss ich auch haben!"
- Der Kunde als Verbraucher soll Vertrauen gewinnen, die Daten sollen gut sichtbar sein, aber nicht verkitscht wie eine Urkunde bei einer Kaffeefahrt. Der Verbraucher geht auf das Zertifikat und kommt zur Urkunde, deshalb soll die Farbe, und Darstellung, Seriosität des Unternehmens ausstrahlen.
Sonstiges
- Die Urkunde soll dem neuen Design unserer Seite (zu sehen unter: http://mein-siegelwerk.de) angepasst sein.
- Vor Auftragsendvergabe erhalten Sie noch ein telefonisches Briefing über unsere Erfahrungswerte
Link zur bestehenden alten Webseite (Altes Design): http://gruen-im-herbst.de
Info Verbraucher: http://www.gruen-im-herbst.de/verbraucher/
Info zum Zertifikat: http://www.gruen-im-herb..

```html
<!DOCTYPE html>
<html lang="de">
<head>
<meta charset="utf-8">
<title>Zertifikat – Grün im Herbst</title>
<link rel="stylesheet" href="https://fonts.googleapis.com/css2?family=Raleway:wght@200;300;400;600&display=swap">
<style>
  :root {
    --paper-light: #f7f1e8;
    --paper-mid: #ece2d3;
    --paper-edge: #dccdb7;
    --frame: #b9a587;
    --frame-soft: #d3c3aa;
    --title: #6e5a3e;
    --label: #7a6446;
    --value: #3a3128;
    --seal-ring: #c9c4bd;
    --seal-face: #f4f2ef;
    --signature: #cbbda6;
  }
  * { margin: 0; padding: 0; box-sizing: border-box; }
  html, body { width: 850px; height: 1200px; overflow: hidden; }
  body { font-family: "Raleway", sans-serif; }

  .certificate {
    position: relative;
    width: 850px;
    height: 1200px;
    background:
      repeating-linear-gradient(-35deg, rgba(255,255,255,0.18) 0 2px, rgba(255,255,255,0) 2px 7px),
      radial-gradient(ellipse at 50% 40%, var(--paper-light) 0%, var(--paper-mid) 60%, var(--paper-edge) 100%);
    overflow: hidden;
  }

  .frame { position: absolute; inset: 0; }

  .certificate__title {
    position: absolute;
    top: 102px;
    left: 0;
    width: 850px;
    text-align: center;
    font-weight: 200;
    font-size: 116px;
    letter-spacing: 2px;
    line-height: 1;
    color: var(--title);
  }
  .certificate__program {
    position: absolute;
    top: 222px;
    left: 0;
    width: 850px;
    text-align: center;
    font-weight: 300;
    font-size: 44px;
    line-height: 1;
    color: var(--title);
  }

  .details {
    position: absolute;
    top: 322px;
    left: 0;
    width: 850px;
    font-size: 24px;
    line-height: 30px;
  }
  .details__row { display: flex; margin-bottom: 27px; }
  .details__row--tight { margin-bottom: 12px; }
  .details__label {
    width: 348px;
    text-align: right;
    font-weight: 600;
    color: var(--label);
  }
  .details__value {
    padding-left: 12px;
    font-weight: 300;
    color: var(--value);
  }

  .approval__label {
    position: absolute;
    top: 922px;
    left: 0;
    width: 348px;
    text-align: right;
    font-size: 24px;
    font-weight: 600;
    color: var(--label);
  }
  .approval__signatures {
    position: absolute;
    top: 972px;
    left: 150px;
    width: 320px;
    height: 72px;
    border-radius: 36px;
    background: linear-gradient(90deg, rgba(203,189,166,0.15), rgba(203,189,166,0.45), rgba(203,189,166,0.15));
  }
  .approval__name {
    position: absolute;
    top: 1040px;
    font-size: 17px;
    font-weight: 400;
    color: var(--value);
  }
  .approval__name--first { left: 163px; }
  .approval__name--second { left: 308px; }

  .seal { position: absolute; top: 872px; left: 474px; }
</style>
</head>
<body>
<main class="certificate">
  <svg class="frame" width="850" height="1200" viewBox="0 0 850 1200" aria-hidden="true">
    <rect x="60" y="60" width="730" height="1080" fill="none" stroke="var(--frame)" stroke-width="2"/>
    <rect x="72" y="72" width="706" height="1056" fill="none" stroke="var(--frame-soft)" stroke-width="8"/>
    <rect x="84" y="84" width="682" height="1032" fill="none" stroke="var(--frame)" stroke-width="1.5"/>
    <line x1="84" y1="300" x2="84" y2="880" stroke="var(--frame)" stroke-width="3"/>
    <line x1="766" y1="300" x2="766" y2="880" stroke="var(--frame)" stroke-width="3"/>
  </svg>

  <h1 class="certificate__title">ZERTIFIKAT</h1>
  <p class="certificate__program">GRÜN IM HERBST</p>

  <dl class="details">
    <div class="details__row"><dt class="details__label">Zertifikat ID:</dt><dd class="details__value">7250441e9e</dd></div>
    <div class="details__row"><dt class="details__label">Anbieter:</dt><dd class="details__value">Grün im Herbst<br>Ihr Zertifizierungsdienst</dd></div>
    <div class="details__row"><dt class="details__label">Status:</dt><dd class="details__value">aktiv</dd></div>
    <div class="details__row"><dt class="details__label">Unternehmen:</dt><dd class="details__value">Senioren Service Lindner<br>Birken Str. 7<br>12345 Stadt<br>Deutschland<br>info@lindner-service.org</dd></div>
    <div class="details__row"><dt class="details__label">Vertretungs-<br>berechtigter:</dt><dd class="details__value">Frau Petra<br>Lindner</dd></div>
    <div class="details__row details__row--tight"><dt class="details__label">Erstprüfung am:</dt><dd class="details__value">07.04.2017</dd></div>
    <div class="details__row"><dt class="details__label">gültig bis:</dt><dd class="details__value">07.04.2019</dd></div>
  </dl>

  <p class="approval__label">Bestätigt von:</p>
  <div class="approval__signatures" role="img" aria-label="Handschriftliche Unterschriften der Prüfer"></div>
  <span class="approval__name approval__name--first">K. Lorenz</span>
  <span class="approval__name approval__name--second">B. Adler</span>

  <svg class="seal" width="210" height="210" viewBox="0 0 210 210" role="img" aria-label="Prüfsiegel">
    <circle cx="105" cy="105" r="100" fill="var(--seal-ring)"/>
    <circle cx="105" cy="105" r="70" fill="var(--seal-face)"/>
  </svg>
</main>
</body>
</html>
```